Vela Errands Web Design Project

Homepage components
o Logo
o Rotating header
o Main menu
o Animation video
o Banners
o Members login
o Latest news

The design’s preferred colors are black (background), silver (main tabs) and white (text)

Site map:
• Home
• News
• About us
o Welcome Note
o Company Profile
• Member Log in
o Registered homepage
? Request a service (form)
? Services directory
? Update profile
? Services history
• Member registration
o Registration form
• Partners
Footer Menu
• Contact us
• Terms & Conditions
• Privacy policy
• Social media links
• Sitemap

Brief about the company:
Vela Errands is a Jordanian company dedicated to elevate and redefine the level of service in the country. We are set out to give premium services at affordable prices. In this fast paced environment that we live in, we barely have the luxury of free time anymore and we, at Vela Errands will be giving you that extra hour or two per day to spend as your heart desires!
By becoming a member you will get access to a world of comfort and peace of mind. We have done the homework on your behalf and have established the network of connections that will enable you to live a headache free life.
We will be providing our members with support and assistance in their day to day lives in the fields that consumes and wastes time the most. We are value driven and below is our “ever-growing” list of services that we will provide at excellent prices:
• Maintenance (carpentry, plumbing, electrical, painting, decorating, gardening… etc)
• Cleaning (pre and post tenancy, periodical deep cleaning, packing and moving services, laundry… etc)
• Personalized delivery services (grocery, important documents, office related supplies, posting cheques, food, paying bills… etc)
• Passport, driving license and ID reissuance
• Travel arrangements (flights, hotels, airport transfers… etc)
• Premium car rental services
• Restaurant reservations
• IT assistance
• Event planning and all related services
• Catering arrangements

Aside from all the services we have on offer we have collaborated with a number of places (that we like to call partners) in town where Vela Errands members are entitled to benefits and privileges that will most certainly add value to their membership. Alongside our partners we have come up with the best formula that will please our members. Below are some of our current partners:

Requirements
Must have
• Homepage components
o Logo
o Rotating header
o Main menu
o Animation video
o Banners
o Members login
o Latest news

```html
<!DOCTYPE html>
<html lang="en">
<head>
<meta charset="utf-8">
<title>Vela Errands – Home</title>
<link href="https://fonts.googleapis.com/css2?family=Source+Sans+3:ital,wght@0,300;0,400;0,600;1,400&family=Roboto+Condensed:wght@300;400&display=swap" rel="stylesheet">
<style>
:root{
  --ink:#2b2b2b;
  --text:#555;
  --muted:#888;
  --nav-dark:#2e2e2e;
  --line:#5a5a5a;
  --footer:#363636;
  --footer-text:#d0d0d0;
  --white:#fff;
  --ad-green:#5fae3a;
  --ad-light:#8cc866;
  --ad-warm:#ead9c2;
}
*{box-sizing:border-box;margin:0;padding:0}
html,body{width:984px;height:1200px;overflow:hidden}
body{position:relative;background:var(--white);font-family:"Source Sans 3",sans-serif;color:var(--text)}
.abs{position:absolute}

.masthead{left:0;top:0;width:984px;height:164px;background:linear-gradient(#efefef,#f6f6f6 80%,#fff)}
.brand{left:42px;top:26px}
.brand-name{font-size:44px;font-weight:300;color:var(--ink);letter-spacing:.5px;line-height:1;display:flex;align-items:center;gap:10px}
.brand-dot{width:12px;height:12px;border-radius:50%;background:var(--ink)}
.brand-tag{font-size:15px;color:var(--muted);margin:6px 0 0 38px;letter-spacing:.5px}

.login{left:689px;top:16px;width:242px}
.login h3{font-size:16px;font-weight:400;color:#555;display:flex;align-items:center;gap:8px}
.login label{position:absolute;left:0;font-size:11px;font-style:italic;color:#777}
.login .field{position:absolute;left:73px;width:169px;height:23px;background:#fff;border:1px solid #c9c9c9;border-radius:2px}
.login .btn{position:absolute;left:196px;top:92px;width:45px;height:20px;background:linear-gradient(#7a7a7a,#4a4a4a);color:#fff;font-size:11px;font-style:italic;font-weight:600;text-align:center;line-height:20px;border-radius:2px}

.mainnav{left:42px;top:146px;width:898px;height:36px;border-radius:18px;background:linear-gradient(#5c5c5c,var(--nav-dark) 55%,#1f1f1f);display:flex;align-items:center}
.mainnav .home{width:58px;height:36px;display:flex;align-items:center;justify-content:center;border-right:1px solid var(--line)}
.mainnav a{color:#eee;font-size:13px;text-decoration:none;padding:0 17px;height:36px;line-height:36px;border-right:1px solid var(--line)}
.mainnav .search{position:absolute;left:707px;top:8px;width:176px;height:21px;border-radius:11px;background:#fff}

.slider{left:42px;top:200px;width:900px;height:280px;background:linear-gradient(90deg,#e9e9e9,#f6f6f6 55%,#d6d6d6);overflow:hidden}
.slide-photo{position:absolute;left:50px;top:0;width:400px;height:280px;background:radial-gradient(ellipse at 50% 55%,#8a8a8a,#bdbdbd 55%,rgba(220,220,220,0))}
.slide-title{position:absolute;left:471px;top:78px;font-family:"Roboto Condensed",sans-serif;font-weight:300;font-size:31px;color:#222}
.slider-base{left:42px;top:478px;width:900px;height:3px;background:#1f1f1f}
.slider-shadow{left:60px;top:481px;width:864px;height:14px;background:radial-gradient(ellipse at 50% 0,rgba(0,0,0,.22),rgba(0,0,0,0) 70%)}

.welcome{left:43px;top:512px;width:583px}
.welcome h1{font-size:22px;font-weight:400;color:var(--ink);margin-bottom:12px}
.welcome p{font-size:11.8px;line-height:20.6px;text-align:justify;color:#666}

.video{left:652px;top:512px;width:286px;height:163px;background:#111;padding:3px}
.video-screen{position:relative;width:280px;height:140px;background:linear-gradient(90deg,#c8c8c8,#9c9c9c)}
.video-logo{position:absolute;left:22px;top:22px;font-size:24px;font-weight:300;color:#222}
.video-person{position:absolute;right:0;top:10px;width:110px;height:130px;background:radial-gradient(ellipse at 50% 45%,#5a5a5a,rgba(120,120,120,0) 70%)}
.video-play{position:absolute;left:126px;top:60px;width:30px;height:20px;background:#111;border-radius:3px}
.video-bar{position:relative;height:16px}
.video-shadow{left:660px;top:675px;width:270px;height:10px;background:radial-gradient(ellipse at 50% 0,rgba(0,0,0,.2),rgba(0,0,0,0) 70%)}

.services-title{left:44px;top:719px;font-size:17px;font-weight:400;color:var(--ink)}
.services{list-style:none;font-size:12.3px;line-height:17px;color:#444}
.services li{position:relative;padding-left:17px;margin-bottom:17px}
.services li svg{position:absolute;left:0;top:4px}
.col-a{left:41px;top:760px;width:302px}
.col-b{left:373px;top:760px;width:262px}

.news{left:625px;top:704px;width:318px;height:264px;background:linear-gradient(#f0f0f0,#fafafa)}
.news h2{position:absolute;left:16px;top:16px;font-size:17px;font-weight:400;color:var(--ink)}
.news .rule{position:absolute;left:18px;top:47px;width:286px;border-top:1px dotted #777}
.news article{position:absolute;left:21px;width:283px}
.news h4{font-size:13px;font-style:italic;font-weight:400;color:#333}
.news time{display:block;font-size:10.8px;font-style:italic;color:#555;margin:1px 0 10px}
.news p{font-size:11px;line-height:15px;color:#555;text-align:justify}

.ad{left:151px;top:982px;width:682px;height:84px;border:1px solid #555;background:linear-gradient(90deg,#fff 0,#fff 17%,var(--ad-green) 23%,var(--ad-light) 78%,var(--ad-warm) 86%,var(--ad-warm) 100%)}

.footer{left:0;top:1081px;width:984px;height:119px;background:var(--footer);border-top:3px solid #5a5a5a;color:var(--footer-text)}
.footer-brand{left:47px;top:50px;font-size:24px;font-weight:300;color:#9a9a9a}
.contact{left:213px;top:16px;font-size:11px;line-height:17px}
.contact h3{font-size:17px;font-weight:400;color:#fff;display:flex;align-items:center;gap:10px;margin-bottom:8px}
.footlinks{list-style:none;font-size:12px;line-height:19.7px}
.footlinks li::before{content:"";display:inline-block;width:4px;height:4px;border-radius:50%;background:#aaa;margin:0 10px 2px -14px}
.links-a{left:470px;top:13px}
.links-b{left:565px;top:13px}
.copyright{left:720px;top:14px;width:218px;text-align:center;font-size:11px;line-height:23px}
.social{left:800px;top:72px;display:flex;gap:7px}
.social span{width:26px;height:26px;border-radius:50%;background:#fff}
</style>
</head>
<body>

<header class="masthead abs"></header>

<div class="brand abs">
  <div class="brand-name"><span class="brand-dot"></span>Vela Errands</div>
  <div class="brand-tag">we make life easier</div>
</div>

<form class="login abs" aria-label="Member login">
  <h3><svg width="16" height="16" viewBox="0 0 16 16"><circle cx="8" cy="5" r="4" fill="#555"/><path d="M0 16c0-5 3-7 8-7s8 2 8 7z" fill="#555"/></svg>Member Login</h3>
  <label style="top:36px">Username :</label><span class="field" style="top:30px"></span>
  <label style="top:68px">Password :</label><span class="field" style="top:62px"></span>
  <span class="btn">Login</span>
</form>

<nav class="mainnav abs">
  <span class="home"><svg width="16" height="14" viewBox="0 0 16 14"><path d="M8 0L0 7h2v7h4V9h4v5h4V7h2z" fill="#fff"/></svg></span>
  <a>About us</a><a>News</a><a>Partners</a><a>Login</a><a>Register</a><a style="border:0">Contact us</a>
  <span class="search"><svg style="position:absolute;right:8px;top:4px" width="13" height="13" viewBox="0 0 13 13"><circle cx="5" cy="5" r="4" fill="none" stroke="#777" stroke-width="1.5"/><path d="M8 8l4 4" stroke="#777" stroke-width="1.5"/></svg></span>
</nav>

<section class="slider abs">
  <div class="slide-photo" role="img" aria-label="Photo of a cheering man at a laptop"></div>
  <div class="slide-title">Excepteur sint occaecat cupidatat</div>
  <svg style="position:absolute;left:380px;top:246px" width="170" height="34" viewBox="0 0 170 34">
    <path d="M0 34C15 34 12 0 30 0h110c18 0 15 34 30 34z" fill="#3a3a3a"/>
    <circle cx="41" cy="18" r="6" fill="#eee"/><circle cx="67" cy="18" r="6" fill="#111"/><circle cx="93" cy="18" r="6" fill="#111"/><circle cx="119" cy="18" r="6" fill="#111"/>
  </svg>
</section>
<div class="slider-base abs"></div>
<div class="slider-shadow abs"></div>

<section class="welcome abs">
  <h1>Welcome to our site</h1>
  <p>Sed ut perspiciatis unde omnis iste natus error sit voluptatem accusantium doloremque laudantium, totam rem aperiam, eaque ipsa quae ab illo inventore veritatis et quasi architecto beatae vitae dicta sunt explicabo. Nemo enim ipsam voluptatem quia voluptas sit aspernatur aut odit aut fugit, sed quia consequuntur magni dolores eos qui ratione voluptatem sequi nesciunt. Neque porro quisquam est, qui dolorem ipsum quia dolor sit amet, consectetur, adipisci velit, sed quia non numquam eius modi tempora incidunt ut labore et dolore magnam aliquam quaerat voluptatem.</p>
</section>

<div class="video abs">
  <div class="video-screen">
    <div class="video-person" role="img" aria-label="Video still of a thoughtful man"></div>
    <div class="video-logo">Vela Errands</div>
    <div class="video-play"><svg width="30" height="20" viewBox="0 0 30 20"><path d="M11 4l10 6-10 6z" fill="#fff"/></svg></div>
  </div>
  <svg class="video-bar" width="280" height="16" viewBox="0 0 280 16">
    <rect y="0" width="280" height="3" fill="#555"/><rect y="0" width="66" height="3" fill="#d1141b"/><circle cx="66" cy="1.5" r="3" fill="#eee"/>
    <rect x="6" y="7" width="2" height="6" fill="#ccc"/><rect x="10" y="7" width="2" height="6" fill="#ccc"/>
    <path d="M26 8h3l3-2v8l-3-2h-3z" fill="#ccc"/>
    <rect x="262" y="7" width="7" height="6" fill="none" stroke="#ccc"/>
  </svg>
</div>
<div class="video-shadow abs"></div>

<h2 class="services-title abs">Our Services</h2>
<svg width="0" height="0" style="position:absolute"><defs><symbol id="arrow" viewBox="0 0 10 8"><path d="M0 3h5V0l5 4-5 4V5H0z" fill="#999"/></symbol></defs></svg>
<ul class="services col-a abs">
  <li><svg width="10" height="8"><use href="#arrow"/></svg>Maintenance (carpentry, plumbing, electrical, painting, decorating, gardening… etc)</li>
  <li><svg width="10" height="8"><use href="#arrow"/></svg>Cleaning (pre and post tenancy, periodical deep cleaning, packing and moving services, laundry… etc)</li>
  <li><svg width="10" height="8"><use href="#arrow"/></svg>Personalized delivery services (grocery, important documents, office related supplies, posting cheques, food, paying bills… etc)</li>
  <li><svg width="10" height="8"><use href="#arrow"/></svg>Travel arrangements (flights, hotels, airport transfers… etc)</li>
</ul>
<ul class="services col-b abs">
  <li><svg width="10" height="8"><use href="#arrow"/></svg>Premium car rental services</li>
  <li><svg width="10" height="8"><use href="#arrow"/></svg>Restaurant reservations</li>
  <li><svg width="10" height="8"><use href="#arrow"/></svg>IT assistance</li>
  <li><svg width="10" height="8"><use href="#arrow"/></svg>Event planning and all related services</li>
  <li><svg width="10" height="8"><use href="#arrow"/></svg>Catering arrangements</li>
  <li><svg width="10" height="8"><use href="#arrow"/></svg>Passport, driving license and ID reissuance</li>
</ul>

<aside class="news abs">
  <h2>Latest News</h2>
  <div class="rule"></div>
  <article style="top:66px">
    <h4>Duis aute reprehenderit</h4>
    <time>June 7th, 2012</time>
    <p>Voluptate velit esse cillum dolore eu fugiat nulla pariatur. Excepteur sint occaecat cupidatat.</p>
  </article>
  <article style="top:161px">
    <h4>Duis aute reprehenderit</h4>
    <time>June 7th, 2012</time>
    <p>Voluptate velit esse cillum dolore eu fugiat nulla pariatur. Excepteur sint occaecat cupidatat.</p>
  </article>
</aside>

<div class="ad abs" role="img" aria-label="Advertising banner space"></div>

<footer class="footer abs">
  <div class="footer-brand abs">Vela Errands</div>
  <div class="contact abs">
    <h3><svg width="22" height="22" viewBox="0 0 22 22"><rect width="22" height="22" rx="3" fill="#777"/><path d="M7 5c-2 1-2 4 1 8s6 5 7 4l1-2-3-2-1 1c-1 0-3-2-3-3l1-1-2-3z" fill="#333"/></svg>Contact Details</h3>
    #12 Cedar Road, Lorem ipsum,<br>Phone: 555 210 4471<br>Tollfree: (006) 51870293<br>E-mail: info@velaerrands.com
  </div>
  <ul class="footlinks links-a abs"><li>Home</li><li>News</li><li>About us</li><li>Login</li><li>Register</li></ul>
  <ul class="footlinks links-b abs"><li>Partners</li><li>Contact us</li><li>Terms &amp; conditions</li><li>Privacy Policy</li><li>Site map</li></ul>
  <div class="copyright abs">Copyright © 2012 www.velaerrands.com<br>All rights reserved.</div>
  <div class="social abs" aria-label="Social media links"><span></span><span></span></div>
</footer>

</body>
</html>
```